Company Banner

I would like our 5 corporate Core Values placed on a single banner that has a theme related to our engineering industry.

Core Values: Productive & Hard Working, Professional, Humble, Personable, Adaptable

Target Market(s)

Construction, Engineering

Requirements
Must have
• All words randomly positioned on the banner with color and industry background images.

Please add company logo to upper left corner as well (attached logo design file)

```html
<!DOCTYPE html>
<html lang="en">
<head>
<meta charset="utf-8">
<title>Core Values Banner</title>
<link href="https://fonts.googleapis.com/css2?family=Roboto:wght@400;700&display=swap" rel="stylesheet">
<style>
  :root {
    --sky-top: #9fbfdf;
    --sky-mid: #c9d9e8;
    --plant: #a9a194;
    --panel: #f2f2f2;
    --label-bg: rgba(244, 244, 244, 0.92);
    --label-text: #3b3b3b;
    --brand-text: #3f4449;
  }
  * { margin: 0; padding: 0; box-sizing: border-box; }
  html, body { width: 1200px; height: 675px; overflow: hidden; }
  .banner {
    position: relative;
    width: 1200px;
    height: 675px;
    overflow: hidden;
    font-family: "Roboto", Arial, sans-serif;
  }
  .backdrop {
    position: absolute; inset: 0;
    background:
      radial-gradient(ellipse 520px 120px at 700px 60px, rgba(255,255,255,0.85), transparent 70%),
      radial-gradient(ellipse 300px 90px at 180px 180px, rgba(255,255,255,0.7), transparent 70%),
      linear-gradient(180deg, var(--sky-top) 0%, var(--sky-mid) 45%, #c8c4ba 70%, var(--plant) 100%);
  }
  .corner-panel { position: absolute; left: 0; top: 0; }
  .brand {
    position: absolute;
    left: 36px; top: 58px;
    display: flex;
    align-items: center;
    gap: 9px;
    color: var(--brand-text);
    font-weight: 700;
    font-size: 21px;
    line-height: 24px;
    white-space: nowrap;
  }
  .brand-square {
    width: 14px; height: 14px;
    background: var(--brand-text);
  }
  .photo {
    position: absolute;
    width: 300px; height: 181px;
    box-shadow: 0 2px 6px rgba(0,0,0,0.2);
  }
  .photo--welding { left: 272px; top: 138px; background: radial-gradient(circle at 75% 75%, #fff3d6 0%, #e6a55a 18%, #3b3a4a 55%, #1f2b3b 100%); }
  .photo--workshop { left: 655px; top: 138px; background: linear-gradient(120deg, #c9c7c0 0%, #8e8474 45%, #4a3e34 100%); }
  .photo--cutting { left: 102px; top: 402px; background: radial-gradient(circle at 20% 20%, #fff6e8 0%, #b8846a 20%, #4b5870 60%, #2e3a30 100%); }
  .photo--mechanic { left: 483px; top: 402px; background: linear-gradient(135deg, #4a4036 0%, #6d5c4c 50%, #3a2f28 100%); }
  .photo--site { left: 873px; top: 402px; background: linear-gradient(135deg, #c9a22e 0%, #6b5a3a 45%, #3c3f4c 100%); }
  .value {
    position: absolute;
    background: var(--label-bg);
    color: var(--label-text);
    font-weight: 700;
    font-size: 43px;
    line-height: 41px;
    letter-spacing: -0.06em;
    padding: 0 9px;
    display: flex;
    align-items: center;
    white-space: nowrap;
  }
  .value--productive { left: 205px; top: 181px; width: 259px; height: 100px; padding-left: 11px; }
  .value--professional { left: 579px; top: 197px; width: 235px; height: 63px; padding-left: 15px; }
  .value--humble { left: 16px; top: 461px; width: 154px; height: 63px; }
  .value--personable { left: 412px; top: 461px; width: 209px; height: 63px; }
  .value--adaptable { left: 793px; top: 461px; width: 200px; height: 63px; }
</style>
</head>
<body>
<div class="banner">
  <div class="backdrop" role="img" aria-label="Blurred industrial plant with smokestacks under a cloudy blue sky"></div>

  <svg class="corner-panel" width="330" height="160" viewBox="0 0 330 160" aria-hidden="true">
    <polygon points="0,0 326,0 172,156 0,156" fill="var(--panel)"/>
  </svg>
  <div class="brand"><span class="brand-square"></span>Brightforge Works</div>

  <div class="photo photo--welding" role="img" aria-label="Welder at work with sparks flying"></div>
  <div class="photo photo--workshop" role="img" aria-label="Technician working at a workshop bench"></div>
  <div class="photo photo--cutting" role="img" aria-label="Worker with face shield cutting metal"></div>
  <div class="photo photo--mechanic" role="img" aria-label="Mechanic in hard hat repairing an engine"></div>
  <div class="photo photo--site" role="img" aria-label="Construction worker carrying a hose on site"></div>

  <div class="value value--productive">Productive &amp;<br>Hard Working</div>
  <div class="value value--professional">Professional</div>
  <div class="value value--humble">Humble</div>
  <div class="value value--personable">Personable</div>
  <div class="value value--adaptable">Adaptable</div>
</div>
</body>
</html>
```